New Wine Label - Classy, Simple, Modern

We are a small boutique winery who have been making and selling wine for 21 years. We are called "Velmoran Winery" and Velmoran is the Greek God of wine. We have a classic label at the moment that we would like to modernise.

We are looking to update our labels while keeping some of the original elements.
From existing label to definitely keep:
1. Logo (Colour can be darkened to a very dark purple - almost black)
2. Legal requirements - Front Label: 750ml, variety, year, "Canberra District" Back Label: Produce of Australia, number of standard drinks, alc/vol, additives, internet address, bar code plus new requirement to warn pregnant women alcohol can harm their babies.
From existing label open to change:
3. What would be nice - Separate front and back labels. Focus on logo on front label (Possibly printed in a raised gloss/embossed), Modern Font,
4. What can we lose? Happy to lose the words about us.
5.Font - Modern, Colour - white background, Shape Rectangular Front approximately height 11cm width 9cm & Back height 9cm width 7cm.

Prototype label can be for a
Front:
2022 Cabernet Sauvignon, Canberra District, 750ml, Estate Grown and Made
Back
13.6%ALC/VOL, APPROX 8.0 STANDARD DRINKS, PRESERVATIVE (220) ADDED, PRODUCE OF AUSTRALIA, Bar Code, Pregnant women warning, www.velmoran-winery.com.au

if you want to use some words to describe the wine that's fine - you can make some up or use existing words from our website www.velmoran-winery.com.au

Files:
1 - Photo of existing front label
2 - Current printers spec sheet for front and back label
3 - Pregnancy warning graphic (specific details see link below - label type 1)
4 - Current Bar Code for Cabernet Sauvignon
Many file types of existing logo

Link to legal requirement for pregnant women warning - we need label type 1 -https://www.trelvacorp.gov.au/sector/packaging/Pages/caution-notice-labels-downloadable-files.aspx

25 - 40 year olds, drink wine

Winery - Wine Production

```html
<!DOCTYPE html>
<html lang="en">
<head>
<meta charset="utf-8">
<title>Velmoran Winery – Cabernet Sauvignon Front Label</title>
<link rel="stylesheet" href="https://fonts.googleapis.com/css2?family=Marcellus&family=Open+Sans:wght@300;400&display=swap">
<style>
  :root {
    --backdrop: #3a3b40;
    --backdrop-edge: #2a2b2f;
    --label-white: #ffffff;
    --label-shade: #ecedee;
    --ink: #1e1e20;
    --ink-soft: #4a4a4e;
    --gold: #c9a24a;
    --gold-deep: #a9822f;
  }
  * { box-sizing: border-box; margin: 0; padding: 0; }
  html, body {
    width: 1200px;
    height: 900px;
    overflow: hidden;
  }
  body {
    background: radial-gradient(ellipse at 50% 55%, var(--backdrop) 0%, var(--backdrop-edge) 100%);
    display: flex;
    align-items: center;
    justify-content: center;
  }
  .front-label {
    width: 540px;
    height: 660px;
    background: linear-gradient(180deg, var(--label-white) 0%, var(--label-white) 70%, var(--label-shade) 100%);
    display: flex;
    flex-direction: column;
    align-items: center;
    padding-top: 78px;
    color: var(--ink);
    text-align: center;
  }
  .brand-mark {
    width: 62px;
    height: 62px;
    margin-bottom: 22px;
  }
  .winery-name {
    font-family: "Marcellus", serif;
    font-size: 21px;
    letter-spacing: 0.06em;
    text-transform: uppercase;
    color: var(--ink);
    margin-bottom: 48px;
  }
  .region {
    font-family: "Open Sans", sans-serif;
    font-weight: 300;
    font-size: 19px;
    letter-spacing: 0.12em;
    color: var(--ink-soft);
    margin-bottom: 10px;
  }
  .variety {
    font-family: "Marcellus", serif;
    font-size: 44px;
    line-height: 0.95;
    letter-spacing: 0.02em;
    text-transform: uppercase;
    color: var(--ink);
    margin-bottom: 68px;
  }
  .vintage {
    font-family: "Open Sans", sans-serif;
    font-weight: 300;
    font-size: 46px;
    letter-spacing: 0.08em;
    color: var(--ink);
  }
  .volume {
    margin-top: auto;
    margin-bottom: 70px;
    font-family: "Open Sans", sans-serif;
    font-weight: 300;
    font-size: 22px;
    letter-spacing: 0.14em;
    color: var(--ink-soft);
  }
</style>
</head>
<body>
  <main class="front-label">
    <svg class="brand-mark" viewBox="0 0 62 62" aria-hidden="true">
      <defs>
        <linearGradient id="gold-fill" x1="0" y1="0" x2="1" y2="1">
          <stop offset="0" stop-color="var(--gold)"/>
          <stop offset="1" stop-color="var(--gold-deep)"/>
        </linearGradient>
      </defs>
      <circle cx="31" cy="31" r="30" fill="url(#gold-fill)"/>
    </svg>
    <p class="winery-name">Velmoran Winery</p>
    <p class="region">Canberra district</p>
    <h1 class="variety">Cabernet<br>Sauvignon</h1>
    <p class="vintage">2122</p>
    <p class="volume">750ml</p>
  </main>
</body>
</html>
```